Family owned plumbing contractor needs eye catching business card design

Business cards that are unique, eye catching, and provide customers with general company information, such as name, address, phone number, website, employee name/title, cell phone #, & email address. We are transitioning to a new logo that utilizes a more retro feel, so we are interested in seeing some cool old school designs in the mix. We are liking the dark background on some of the samples on this website. If that is workable with our artwork, we would like to see that incorporated into the design.
Contact Information for Business Card
Copperline Pipeworks, Inc.
www.copperlinepipeworks.example
(555) 392-7068 phone
Nevada License #64205
California License #5810473
Dale Wrennick, President
(555) 618-9032 cell
dale@copperlinepipeworks.example
Residential * Commercial * Service
Requirements
Must have
- The business card details listed above & logo provided.
Nice to have
- I made some notes about color options in the description.

```html
<!DOCTYPE html>
<html lang="en">
<head>
<meta charset="utf-8">
<title>Copperline Pipeworks – Business Card</title>
<link rel="stylesheet" href="https://fonts.googleapis.com/css2?family=Arvo:wght@400;700&family=Lobster&display=swap">
<style>
  :root{
    --backdrop:#dcdedf;
    --card:#2b2b2b;
    --blue:#4e7fa6;
    --teal:#86d6c6;
    --white:#f2f2f2;
    --dots:#d8d8d8;
  }
  html,body{margin:0;padding:0;overflow:hidden;}
  body{width:1200px;height:800px;background:var(--backdrop);position:relative;font-family:"Arvo",serif;}
  .card{position:absolute;left:285px;width:630px;height:360px;background:var(--card);box-shadow:0 6px 18px rgba(0,0,0,.25);}
  .card--front{top:24px;}
  .card--back{top:408px;}

  /* front */
  .brand{position:absolute;left:0;right:0;top:110px;text-align:center;}
  .brand__mark{display:inline-block;width:26px;height:26px;border-radius:50%;background:var(--teal);vertical-align:middle;margin-right:14px;}
  .brand__name{font-family:"Arvo",serif;font-weight:700;font-size:34px;color:var(--blue);vertical-align:middle;}
  .services{position:absolute;left:0;right:0;top:240px;text-align:center;font-family:"Lobster",cursive;font-size:26px;color:var(--blue);}
  .services__sep{display:inline-block;width:9px;height:9px;background:var(--teal);margin:0 14px;vertical-align:middle;}

  /* back */
  .person{position:absolute;left:0;right:0;top:58px;text-align:center;}
  .person__name{font-family:"Lobster",cursive;font-size:44px;color:var(--blue);line-height:1;}
  .person__title{font-size:17px;color:var(--teal);margin-top:2px;}
  .ribbon{position:absolute;left:55px;top:150px;width:520px;height:44px;}
  .ribbon svg{position:absolute;inset:0;}
  .ribbon__numbers{position:absolute;inset:0;display:flex;justify-content:center;align-items:center;gap:18px;color:var(--white);font-size:21px;}
  .ribbon__divider{width:1px;height:26px;background:var(--teal);opacity:.7;}
  .ribbon__icon{width:16px;height:18px;margin-right:6px;vertical-align:-2px;}
  .licenses{position:absolute;left:0;right:0;top:222px;text-align:center;color:var(--white);font-size:15px;}
  .contact-rule{position:absolute;top:266px;height:0;border-top:2px dotted var(--dots);}
  .contact-rule--left{left:40px;width:225px;}
  .contact-rule--right{right:40px;width:225px;}
  .contact-icons{position:absolute;left:275px;top:253px;display:flex;gap:8px;}
  .contact-icons svg{width:26px;height:26px;}
  .contact{position:absolute;left:0;right:0;top:290px;text-align:center;font-size:16px;line-height:1.35;}
  .contact__email{color:var(--white);}
  .contact__web{color:var(--teal);}
</style>
</head>
<body>
  <section class="card card--front">
    <div class="brand"><span class="brand__mark"></span><span class="brand__name">Copperline Pipeworks, Inc.</span></div>
    <div class="services">Residential<span class="services__sep"></span>Commercial<span class="services__sep"></span>Service</div>
  </section>

  <section class="card card--back">
    <div class="person">
      <div class="person__name">Dale Wrennick</div>
      <div class="person__title">President</div>
    </div>

    <div class="ribbon">
      <svg viewBox="0 0 520 44" preserveAspectRatio="none" aria-hidden="true">
        <polygon points="0,0 520,0 506,22 520,44 0,44 14,22" fill="var(--blue)"/>
      </svg>
      <div class="ribbon__numbers">
        <span><svg class="ribbon__icon" viewBox="0 0 16 18"><path d="M3 1l3 0 1 4-2 1.5c1 2.5 2.5 4 5 5L11.5 9.5l4 1v3c-7 1-14-6-12.5-12.5z" fill="var(--teal)"/></svg>(555) 392-7068</span>
        <span class="ribbon__divider"></span>
        <span><svg class="ribbon__icon" viewBox="0 0 16 18"><rect x="3" y="1" width="10" height="16" rx="2" fill="none" stroke="var(--teal)" stroke-width="1.6"/><line x1="6" y1="14" x2="10" y2="14" stroke="var(--teal)" stroke-width="1.4"/></svg>(555) 618-9032</span>
      </div>
    </div>

    <div class="licenses">Nevada License #64205 &nbsp;•&nbsp; California License #5810473</div>

    <div class="contact-rule contact-rule--left"></div>
    <div class="contact-icons">
      <svg viewBox="0 0 26 26" aria-label="Email"><circle cx="13" cy="13" r="13" fill="var(--teal)"/><rect x="6.5" y="8.5" width="13" height="9" fill="none" stroke="var(--card)" stroke-width="1.5"/><polyline points="6.5,8.5 13,14 19.5,8.5" fill="none" stroke="var(--card)" stroke-width="1.5"/></svg>
      <svg viewBox="0 0 26 26" aria-label="Website"><circle cx="13" cy="13" r="13" fill="var(--teal)"/><circle cx="13" cy="13" r="7" fill="none" stroke="var(--card)" stroke-width="1.5"/><ellipse cx="13" cy="13" rx="3" ry="7" fill="none" stroke="var(--card)" stroke-width="1.3"/><line x1="6" y1="13" x2="20" y2="13" stroke="var(--card)" stroke-width="1.3"/></svg>
    </div>
    <div class="contact-rule contact-rule--right"></div>

    <div class="contact">
      <div class="contact__email">dale@copperlinepipeworks.example</div>
      <div class="contact__web">www.copperlinepipeworks.example</div>
    </div>
  </section>
</body>
</html>
```